Real Estate Website

We currently have an existing site at https://plovermarshdesk.com.au/ but require a much more professional design.

We like the style/design of the following which are competitors : https://tidalquince.com.au/
https://www.ferncaddyhub.com.au/
https://mossylanternco.com.au/

```html
<!DOCTYPE html>
<html lang="en">
<head>
<meta charset="utf-8">
<title>Plover Marsh Desk</title>
<link rel="stylesheet" href="https://fonts.googleapis.com/css2?family=Lato:wght@400;700;900&family=Roboto:wght@400;500;700&display=swap">
<style>
:root{
  --red:#dd3a3d;
  --red-dark:#c9353a;
  --ink:#111;
  --text:#333;
  --muted:#777;
  --plum:#6a2a45;
  --line:#c8c8c8;
  --white:#fff;
  --footer:#0b0b0b;
}
*{margin:0;padding:0;box-sizing:border-box}
html,body{width:1200px;height:3558px;overflow:hidden}
body{position:relative;background:var(--white);font-family:'Roboto',sans-serif;color:var(--text)}
.abs{position:absolute}
/* header */
.brand{position:absolute;display:flex;align-items:center;gap:8px;font-family:'Lato',sans-serif;font-weight:700;font-size:17px;color:var(--plum)}
.brand-mark{width:14px;height:14px;background:var(--red)}
.nav{position:absolute;top:50px;left:0;width:1200px;height:20px;font-size:15px;color:#222}
.nav span{position:absolute;top:0}
/* hero */
.hero{position:absolute;top:133px;left:0;width:1200px;height:600px;background:linear-gradient(180deg,#5d6e62 0%,#8a8d86 35%,#7f7466 60%,#56683c 85%,#4b5d33 100%)}
.hero-shade{position:absolute;inset:0;background:linear-gradient(90deg,rgba(0,0,0,.35),rgba(0,0,0,.05))}
.hero h1{position:absolute;left:86px;top:188px;font-family:'Lato',sans-serif;font-weight:900;font-size:41px;line-height:47px;color:var(--white);text-transform:uppercase;letter-spacing:-.5px}
.btn{position:absolute;background:var(--red);color:var(--white);font-family:'Roboto',sans-serif;font-weight:700;font-size:17px;display:flex;align-items:center;justify-content:center;text-transform:uppercase}
.arrow{position:absolute;top:290px}
/* about */
.sec-title{position:absolute;font-family:'Lato',sans-serif;font-weight:900;text-transform:uppercase;font-size:38px;color:var(--ink)}
.rule{position:absolute;height:3px;background:var(--red)}
.about-text{position:absolute;left:86px;top:934px;width:510px;font-size:14.5px;line-height:25.6px;color:#222}
.about-photo{position:absolute;left:775px;top:826px;width:342px;height:370px;background:radial-gradient(circle at 45% 45%,#f1ece6 0 18%,#b88468 30%,#6d8b38 55%,#3b6a22 100%)}
/* real estate */
.band{position:absolute;top:1287px;left:0;width:1200px;height:790px;background:linear-gradient(180deg,#d94547 0%,#e04a4b 50%,#d9474a 100%)}
.card{position:absolute;top:1478px;width:327px;height:371px;background:var(--white);text-align:center}
.card-art{position:absolute;left:108px;top:38px;width:110px;height:114px;background:linear-gradient(135deg,#f1c9cb,#d9a3b3);border-radius:8px}
.card h3{position:absolute;left:0;width:100%;top:180px;font-family:'Roboto',sans-serif;font-weight:500;font-size:15px;color:#111}
.card p{position:absolute;left:30px;width:267px;top:220px;font-size:14.5px;line-height:25.7px;color:var(--muted)}
.read{position:absolute;left:0;width:100%;top:320px;font-size:15px;color:var(--red);display:flex;justify-content:center;align-items:center;gap:12px}
/* calculator */
.calc{position:absolute;left:86px;top:1958px;width:1031px;height:703px;background:var(--white);border:1px solid #e6b2b3;box-shadow:0 2px 8px rgba(0,0,0,.06)}
.calc h2{position:absolute;top:44px;width:100%;text-align:center;font-family:'Lato',sans-serif;font-weight:700;font-size:38px;color:#111}
.calc .sub{position:absolute;top:108px;width:100%;text-align:center;font-family:'Lato',sans-serif;font-weight:700;font-size:19px;color:var(--red)}
.perk{position:absolute;top:166px;font-family:'Lato',sans-serif;font-size:14.5px;color:#555;display:flex;align-items:center;gap:9px}
.lbl{position:absolute;font-family:'Lato',sans-serif;font-size:14.5px;color:#444;text-transform:uppercase}
.field{position:absolute;height:37px;border:1px solid var(--line);font-family:'Lato',sans-serif;font-size:14.5px;color:#222;display:flex;align-items:center;padding-left:18px}
.total{position:absolute;left:20px;top:615px;width:992px;height:36px;background:var(--red);color:var(--white);font-family:'Lato',sans-serif;font-size:14.5px;display:flex;align-items:center;padding-left:20px}
/* testimonials */
.testi-bg{position:absolute;top:2661px;left:0;width:1200px;height:550px;background:linear-gradient(180deg,#fbfbfc 0%,#eceef2 55%,#dfe2e8 100%)}
.quote{position:absolute;top:2867px;width:395px;height:257px;background:rgba(255,255,255,.85);border:1px solid #e7a9aa}
.avatar{position:absolute;left:47px;top:28px;width:72px;height:72px;border-radius:50%;background:linear-gradient(180deg,#9aa0a8,#3c4250)}
.qname{position:absolute;left:143px;top:44px;font-family:'Lato',sans-serif;font-weight:700;font-size:15px;color:var(--red)}
.stars{position:absolute;left:143px;top:68px;color:#8b87e6;font-size:14px;letter-spacing:5px}
.qtext{position:absolute;left:47px;top:128px;width:320px;font-size:14.5px;line-height:26px;color:#222}
/* footer */
.footer{position:absolute;top:3211px;left:0;width:1200px;height:347px;background:var(--footer);color:var(--white)}
.footer .brand{color:var(--white);left:0;width:1200px;justify-content:center;top:104px}
.fnav{position:absolute;top:165px;font-size:15px}
.fcontact{position:absolute;top:217px;font-size:15px;display:flex;align-items:center;gap:12px}
.fline{position:absolute;left:86px;top:268px;width:1031px;height:1px;background:#444}
.copy{position:absolute;top:297px;width:1200px;text-align:center;font-size:14.5px}
</style>
</head>
<body>

<header>
  <div class="brand" style="left:86px;top:86px"><span class="brand-mark"></span>Plover Marsh Desk</div>
  <nav class="nav">
    <span style="left:333px">Home</span>
    <span style="left:417px">Sell</span>
    <span style="left:482px">Rent</span>
    <span style="left:557px">Add on Service</span>
    <span style="left:702px">Useful Resources</span>
    <span style="left:859px">About</span>
    <span style="left:943px">Contact Us</span>
    <svg class="abs" style="left:1099px;top:1px" width="14" height="14" viewBox="0 0 14 14"><circle cx="6" cy="6" r="4.5" fill="none" stroke="#111" stroke-width="2"/><line x1="9.3" y1="9.3" x2="13" y2="13" stroke="#111" stroke-width="2"/></svg>
  </nav>
</header>

<section class="hero" role="img" aria-label="Two-storey suburban house with double garage, trees and garden shrubs">
  <div class="hero-shade"></div>
  <h1>Help you to sell and rent<br>your home yourself and<br>saving thousands of dollars</h1>
  <div class="btn" style="left:86px;top:361px;width:146px;height:45px">Get Started</div>
  <svg class="arrow" style="left:44px" width="16" height="22" viewBox="0 0 16 22"><polyline points="12,3 4,11 12,19" fill="none" stroke="#fff" stroke-width="3.5"/></svg>
  <svg class="arrow" style="left:1140px" width="16" height="22" viewBox="0 0 16 22"><polyline points="4,3 12,11 4,19" fill="none" stroke="#fff" stroke-width="3.5"/></svg>
</section>

<section class="about">
  <h2 class="sec-title" style="left:86px;top:846px">About Us</h2>
  <div class="rule" style="left:86px;top:899px;width:77px"></div>
  <p class="about-text">Plover Marsh Desk is an Australia real estate expert who can help you to sell, rent &nbsp;your properties yourself and &nbsp;save thousands of dollars at the same time The owner as traditional agent himself found that the landlord always get charged too much for no matter selling, renting &nbsp;their home by the agents. But someone will ask wait can I &nbsp;sell and rent my property by property. these days are looking to buy/rent properties online.</p>
  <div class="btn" style="left:86px;top:1120px;width:136px;height:44px;font-size:16px">Learn More</div>
  <div class="abs" style="left:767px;top:820px;width:85px;height:84px;border-top:5px solid var(--red);border-left:5px solid var(--red)"></div>
  <div class="abs" style="left:1036px;top:1116px;width:86px;height:86px;border-bottom:5px solid var(--red);border-right:5px solid var(--red)"></div>
  <div class="about-photo" role="img" aria-label="Hand holding a small model house above green grass"></div>
</section>

<section class="band" role="img" aria-label="Red-tinted photo of brick homes">
</section>
<h2 class="sec-title" style="left:0;width:1200px;text-align:center;top:1347px;color:#fff">Our Real Estate</h2>
<div class="rule" style="left:561px;top:1423px;width:77px;background:#fff"></div>

<div class="card" style="left:86px">
  <div class="card-art" role="img" aria-label="Line icon of a hand holding money and buildings"></div>
  <h3 style="top:186px">LOREM IPSUM DOLOR &nbsp;AMET</h3>
  <p style="top:222px">Lorem ipsum dolor amet, consectetur adipiscing , sed do eiusmod tempor incididunt ut labore et dolore</p>
  <div class="read" style="top:320px">Read More <svg width="14" height="14" viewBox="0 0 14 14"><circle cx="7" cy="7" r="7" fill="var(--red)"/><polyline points="5.5,4 8.5,7 5.5,10" fill="none" stroke="#fff" stroke-width="2"/></svg></div>
</div>
<div class="card" style="left:438px">
  <div class="card-art" role="img" aria-label="Line icon of a checklist document and a clock"></div>
  <h3>LOREM IPSUM DOLOR &nbsp;AMET</h3>
  <p style="top:216px">Lorem ipsum dolor amet, consectetur adipiscing , sed do eiusmod tempor incididunt ut labore et dolore</p>
  <div class="read" style="top:314px">Read More <svg width="14" height="14" viewBox="0 0 14 14"><circle cx="7" cy="7" r="7" fill="var(--red)"/><polyline points="5.5,4 8.5,7 5.5,10" fill="none" stroke="#fff" stroke-width="2"/></svg></div>
</div>
<div class="card" style="left:789px">
  <div class="card-art" role="img" aria-label="Line icon of an agent beside a house with a rising chart"></div>
  <h3 style="top:183px">LOREM IPSUM DOLOR &nbsp;AMET</h3>
  <p style="top:219px">Lorem ipsum dolor amet, consectetur adipiscing , sed do eiusmod tempor incididunt ut labore et dolore</p>
  <div class="read" style="top:317px">Read More <svg width="14" height="14" viewBox="0 0 14 14"><circle cx="7" cy="7" r="7" fill="var(--red)"/><polyline points="5.5,4 8.5,7 5.5,10" fill="none" stroke="#fff" stroke-width="2"/></svg></div>
</div>

<section class="calc">
  <h2>Sell My Property or Rent My Property</h2>
  <div class="sub">How much could you save by selling with Plover Marsh Desk?</div>
  <div class="perk" style="left:192px"><svg width="14" height="14" viewBox="0 0 14 14"><polyline points="2,7 6,11 12,3" fill="none" stroke="var(--red)" stroke-width="1.8"/></svg>you are in control</div>
  <div class="perk" style="left:384px"><svg width="14" height="14" viewBox="0 0 14 14"><polyline points="2,7 6,11 12,3" fill="none" stroke="var(--red)" stroke-width="1.8"/></svg>easy to use</div>
  <div class="perk" style="left:550px"><svg width="14" height="14" viewBox="0 0 14 14"><polyline points="2,7 6,11 12,3" fill="none" stroke="var(--red)" stroke-width="1.8"/></svg>huge savings</div>
  <div class="perk" style="left:718px"><svg width="14" height="14" viewBox="0 0 14 14"><polyline points="2,7 6,11 12,3" fill="none" stroke="var(--red)" stroke-width="1.8"/></svg>great support</div>

  <div class="lbl" style="left:15px;top:267px">Property Value</div>
  <div class="lbl" style="left:356px;top:267px">Agent Commission (%)</div>
  <div class="lbl" style="left:693px;top:267px">Marketing Fee ($)</div>
  <div class="field" style="left:15px;top:303px;width:308px">$ 700000</div>
  <div class="field" style="left:356px;top:303px;width:308px">2.05</div>
  <div class="field" style="left:700px;top:303px;width:308px">5000</div>

  <div class="lbl" style="left:15px;top:370px">Property Value</div>
  <div class="field" style="left:15px;top:407px;width:994px">19350</div>

  <div class="lbl" style="left:15px;top:474px">Select Our Package</div>
  <div class="field" style="left:15px;top:510px;width:994px">Basic($499)
    <svg class="abs" style="left:930px;top:15px" width="10" height="6" viewBox="0 0 10 6"><polygon points="0,0 10,0 5,6" fill="var(--red)"/></svg>
  </div>

  <div class="lbl" style="left:15px;top:576px">Total Saving With Our Package</div>
  <div class="total">18851</div>
</section>

<section class="testi-bg" role="img" aria-label="Faded city skyline of tall buildings"></section>
<h2 class="sec-title" style="left:0;width:1200px;text-align:center;top:2738px">Our Testimonials</h2>
<div class="rule" style="left:561px;top:2802px;width:77px"></div>

<div class="quote" style="left:184px">
  <div class="avatar" role="img" aria-label="Portrait photo of a client"></div>
  <div class="qname">Jhon Deo</div>
  <div class="stars">★★★★★</div>
  <p class="qtext">Lorem ipsum dolor sit amet, consectetur adipiscing elit, sed do eiusmod tempor incididunt ut labore et dolore magna aliqua. Ut enim ad minim veniam, quis nostrud</p>
</div>
<div class="quote" style="left:621px">
  <div class="avatar" role="img" aria-label="Portrait photo of a client"></div>
  <div class="qname">Jhon Smith</div>
  <div class="stars">★★★★★</div>
  <p class="qtext">Lorem ipsum dolor sit amet, consectetur adipiscing elit, sed do eiusmod tempor incididunt ut labore et dolore magna aliqua. Ut enim ad minim veniam, quis nostrud</p>
</div>

<footer class="footer">
  <div class="brand" style="font-size:16px"><span class="brand-mark" style="background:#fff"></span>Plover Marsh Desk</div>
  <span class="fnav" style="left:335px">Home</span>
  <span class="fnav" style="left:414px">Sell</span>
  <span class="fnav" style="left:477px">Rent</span>
  <span class="fnav" style="left:547px">Add on Service</span>
  <span class="fnav" style="left:688px">About Us</span>
  <span class="fnav" style="left:788px">Contact Us</span>
  <div class="fcontact" style="left:430px"><svg width="12" height="12" viewBox="0 0 12 12"><path d="M2 1l2.5 0 1 3-1.5 1c.8 1.5 1.7 2.4 3 3l1-1.5 3 1V11C5 11 1 7 1 1z" fill="var(--red)"/></svg>1300 555 018</div>
  <div class="fcontact" style="left:602px"><svg width="14" height="11" viewBox="0 0 14 11"><rect x=".75" y=".75" width="12.5" height="9.5" fill="none" stroke="var(--red)" stroke-width="1.5"/><polyline points="1,1 7,6 13,1" fill="none" stroke="var(--red)" stroke-width="1.5"/></svg>info@plovermarshdesk.com.au</div>
  <div class="fline"></div>
  <div class="copy">© Copyright 2021 Real Estate.All right reserved.</div>
</footer>

</body>
</html>
```